Catalog copying current designs, web designs and copywrite.

I am looking for someone to recreate a draft catalog using the same design process.

My entire brief with the photo samples and icons would not fit in here. They are in the google docs folder as below:

https://share.plovimbox.net/folders/7hQwRk2mZaXe9TnB4LpYcVd3sUfGj6K?mode=view

```html
<!DOCTYPE html>
<html lang="en">
<head>
<meta charset="utf-8">
<title>Services – Catalogue Spread</title>
<link rel="stylesheet" href="https://fonts.googleapis.com/css2?family=Roboto:wght@400;500;700;900&display=swap">
<style>
:root{
  --backdrop:#9b9b9b;
  --page:#e9e9ea;
  --page-light:#f4f4f5;
  --brand-red:#8e1b1f;
  --ink-dark:#4a4a4c;
  --ink:#222;
  --ink-soft:#555;
  --white:#fff;
  --photo-grey-a:#8d8d8f;
  --photo-grey-b:#d8d8da;
  --photo-red-a:#a13a32;
  --photo-red-b:#d08a7a;
}
*{box-sizing:border-box;margin:0;padding:0}
html,body{width:1200px;height:1000px;overflow:hidden}
body{background:var(--backdrop);font-family:"Roboto",Arial,sans-serif;position:relative}
.page{position:absolute;top:80px;width:594px;height:840px;overflow:hidden;
  background:linear-gradient(135deg,var(--page-light) 0%,var(--page) 45%,#dcdcde 100%)}
.page--left{left:3px}
.page--right{left:603px}
.page svg.facets,.page svg.art{position:absolute;left:0;top:0}
.abs{position:absolute}
.side-title{position:absolute;left:28px;top:306px;transform-origin:0 0;transform:rotate(-90deg);
  font-weight:900;font-size:56px;letter-spacing:0;color:var(--white);line-height:52px;height:52px;white-space:nowrap}
.page--right .side-title{opacity:.8}
.page-number{position:absolute;right:22px;bottom:16px;font-size:13px;color:#777}
.team-icon{left:110px;top:55px;width:92px;height:34px}
.kicker{left:110px;top:108px;font-weight:900;font-size:22px;color:var(--brand-red);letter-spacing:.5px}
.headline{left:108px;top:124px;font-weight:900;font-size:42px;color:var(--ink-dark);letter-spacing:.5px}
.process-title{left:410px;top:58px;width:170px;text-align:center;font-weight:900;font-size:12.5px;line-height:1.2;color:var(--brand-red)}
.process-intro{left:416px;top:95px;width:164px;text-align:center;font-weight:700;font-size:8.6px;line-height:1.3;color:var(--ink)}
.step{position:absolute;left:433px;width:130px;height:104px;text-align:center}
.step-label{position:absolute;top:10px;left:20px;width:90px;font-weight:700;font-size:8.6px;line-height:1.25;color:var(--ink)}
.step-num{position:absolute;top:43px;left:0;width:130px;font-weight:900;font-size:22px;color:var(--brand-red)}
.positions-title{left:42px;top:634px;font-weight:900;font-size:13px;color:var(--brand-red)}
.positions-title small{font-size:9px;color:var(--ink);font-weight:700}
.position{position:absolute;width:100px;text-align:center;font-weight:900;font-size:8px;line-height:1.2;color:var(--ink-dark)}
.position .glyph{display:block;margin:0 auto 12px;width:20px;height:28px;background:var(--brand-red);border-radius:10px 10px 3px 3px}
.other{left:110px;top:58px;font-weight:500;font-size:31px;color:var(--ink-dark)}
.services-head{left:108px;top:86px;font-weight:900;font-size:54px;color:var(--brand-red);letter-spacing:1px}
.service{position:absolute;width:150px;text-align:center}
.service .glyph{display:block;margin:0 auto 12px;width:46px;height:46px;background:var(--brand-red);border-radius:6px}
.service h3{font-weight:900;font-size:14.5px;color:var(--ink-dark);letter-spacing:.3px;margin-bottom:6px}
.service p{font-size:10px;line-height:1.25;color:var(--ink-soft)}
.service--wide{width:170px}
</style>
</head>
<body>

<section class="page page--left">
  <svg class="facets" width="594" height="840" aria-hidden="true">
    <polygon points="0,0 260,0 120,180" fill="#fff" opacity=".25"/>
    <polygon points="594,600 594,840 420,840" fill="#fff" opacity=".3"/>
    <polygon points="0,560 120,840 0,840" fill="#ccc" opacity=".3"/>
    <polygon points="500,760 594,840 490,840" fill="#fff"/>
  </svg>

  <svg class="art" width="594" height="840">
    <defs>
      <linearGradient id="photoGrey" x1="0" y1="0" x2="1" y2="1">
        <stop offset="0" stop-color="var(--photo-grey-b)"/>
        <stop offset=".5" stop-color="var(--photo-grey-a)"/>
        <stop offset="1" stop-color="var(--photo-grey-b)"/>
      </linearGradient>
      <linearGradient id="photoRed" x1="0" y1="0" x2="1" y2="1">
        <stop offset="0" stop-color="var(--photo-red-b)"/>
        <stop offset="1" stop-color="var(--photo-red-a)"/>
      </linearGradient>
    </defs>
    <polygon role="img" aria-label="Photo of two construction engineers in hard hats reviewing plans on site"
      points="20,185 427,185 300,460 165,580 20,460" fill="url(#photoGrey)"/>
    <polygon role="img" aria-label="Red-toned photo of workers on a construction site"
      points="322,305 420,457 247,457" fill="url(#photoRed)"/>
    <polygon role="img" aria-label="Red-toned photo of construction machinery cabin"
      points="17,468 190,468 103,620" fill="url(#photoRed)"/>
    <g stroke="#fff" stroke-width="1" fill="none" opacity=".8">
      <line x1="60" y1="300" x2="357" y2="160"/>
      <line x1="357" y1="160" x2="180" y2="580"/>
      <line x1="160" y1="200" x2="330" y2="610"/>
      <line x1="330" y1="610" x2="30" y2="480"/>
    </g>
    <polygon points="480,20 516,20 498,46" fill="var(--brand-red)"/>
    <line x1="498" y1="0" x2="498" y2="24" stroke="var(--brand-red)" stroke-width="2"/>
    <g fill="#fff">
      <polygon points="435,168 561,168 498,272"/>
      <polygon points="435,275 561,275 498,379"/>
      <polygon points="435,382 561,382 498,486"/>
      <polygon points="435,489 561,489 498,593"/>
      <polygon points="435,596 561,596 498,700"/>
      <polygon points="435,703 561,703 498,810"/>
    </g>
  </svg>

  <div class="side-title">SERVICES</div>

  <svg class="abs team-icon" viewBox="0 0 92 34" role="img" aria-label="Team icon">
    <g fill="var(--ink-dark)">
      <circle cx="8" cy="14" r="3.5"/><rect x="3" y="19" width="10" height="9" rx="4"/>
      <circle cx="26" cy="7" r="3.5"/><rect x="21" y="12" width="10" height="9" rx="4"/>
      <circle cx="66" cy="7" r="3.5"/><rect x="61" y="12" width="10" height="9" rx="4"/>
      <circle cx="84" cy="14" r="3.5"/><rect x="79" y="19" width="10" height="9" rx="4"/>
    </g>
    <circle cx="46" cy="12" r="6" fill="var(--brand-red)"/>
    <rect x="39" y="20" width="14" height="13" rx="5" fill="var(--brand-red)"/>
  </svg>
  <div class="abs kicker">PERMANENT</div>
  <div class="abs headline">RECRUITMENT</div>

  <div class="abs process-title">OUR RECRUITMENT<br>PROCESS</div>
  <p class="abs process-intro">Our job is to simplify difficulties of recruitment so you can focus on what you do best, it is vital to understand your needs so we can find you the newest addition to your team. Here's a snippet of our process.</p>

  <div class="step" style="top:168px"><span class="step-label">Understanding what you want</span><span class="step-num">1</span></div>
  <div class="step" style="top:275px"><span class="step-label">Screen through candidates</span><span class="step-num">2</span></div>
  <div class="step" style="top:382px"><span class="step-label">Interview the most eligible candidates</span><span class="step-num">3</span></div>
  <div class="step" style="top:489px"><span class="step-label">Perform reference checks</span><span class="step-num">4</span></div>
  <div class="step" style="top:596px"><span class="step-label">Arrange interview</span><span class="step-num">5</span></div>
  <div class="step" style="top:703px"><span class="step-label">Place the Candidate</span><span class="step-num">6</span></div>

  <div class="abs positions-title">POSITIONS WE PROVIDE <small>(BUT NOT LIMITED TO)</small></div>
  <div class="position" style="left:22px;top:664px"><span class="glyph" role="img" aria-label="Construction manager icon"></span>CONSTRUCTION<br>MANAGER</div>
  <div class="position" style="left:114px;top:664px"><span class="glyph" role="img" aria-label="Project manager icon"></span>PROJECT<br>MANAGER</div>
  <div class="position" style="left:207px;top:664px"><span class="glyph" role="img" aria-label="Site manager icon"></span>SITE<br>MANAGER</div>
  <div class="position" style="left:294px;top:664px"><span class="glyph" role="img" aria-label="Foreman icon"></span>FOREMAN</div>
  <div class="position" style="left:22px;top:734px"><span class="glyph" role="img" aria-label="Estimator icon"></span>ESTIMATOR</div>
  <div class="position" style="left:114px;top:734px"><span class="glyph" role="img" aria-label="Contracts administrator icon"></span>CONTRACTS<br>ADMINISTRATOR</div>
  <div class="position" style="left:207px;top:734px"><span class="glyph" role="img" aria-label="Leading hand icon"></span>LEADING<br>HAND</div>
  <div class="position" style="left:294px;top:734px"><span class="glyph" role="img" aria-label="Cadet icon"></span>CADET</div>

  <div class="page-number">7</div>
</section>

<section class="page page--right">
  <svg class="facets" width="594" height="840">
    <defs>
      <radialGradient id="photoBlur" cx=".5" cy=".5" r=".6">
        <stop offset="0" stop-color="#7a7a7c"/>
        <stop offset=".6" stop-color="#b9b9bb"/>
        <stop offset="1" stop-color="#e4e4e6" stop-opacity="0"/>
      </radialGradient>
    </defs>
    <rect role="img" aria-label="Soft-focus photo of a lifting chain and steel beam" x="90" y="140" width="460" height="420" fill="url(#photoBlur)"/>
    <g fill="#fff">
      <polygon points="7,195 322,195 165,475" opacity=".55"/>
      <polygon points="427,80 267,360 587,360" opacity=".55"/>
      <polygon points="9,530 322,530 165,810" opacity=".6"/>
      <polygon points="427,425 269,700 587,700" opacity=".6"/>
      <polygon points="500,760 594,840 490,840" opacity="1"/>
    </g>
  </svg>

  <div class="side-title">SERVICES</div>
  <div class="abs other">OTHER</div>
  <div class="abs services-head">SERVICES</div>

  <div class="service" style="left:90px;top:225px"><span class="glyph" role="img" aria-label="Crane hook icon"></span><h3>RIGGING</h3><p>Lorem ipsum dolor sit amet, consectetur adipiscing elit, sed do eiusmod tempor incididunt ut labore et dolore magna aliqua.</p></div>
  <div class="service service--wide" style="left:342px;top:185px"><span class="glyph" role="img" aria-label="Traffic cone icon"></span><h3>TRAFFIC CONTROL</h3><p>Lorem ipsum dolor sit amet, consectetur adipiscing elit, sed do eiusmod tempor incididunt ut labore et dolore magna aliqua.</p></div>
  <div class="service" style="left:90px;top:565px"><span class="glyph" role="img" aria-label="Cleaning bucket and broom icon"></span><h3>CLEANING</h3><p>Lorem ipsum dolor sit amet, consectetur adipiscing elit, sed do eiusmod tempor incididunt ut labore et dolore magna aliqua.</p></div>
  <div class="service service--wide" style="left:342px;top:525px"><span class="glyph" role="img" aria-label="Mobile crane truck icon"></span><h3>MACHINE HIRE</h3><p>Lorem ipsum dolor sit amet, consectetur adipiscing elit, sed do eiusmod tempor incididunt ut labore et dolore magna aliqua.</p></div>

  <div class="page-number">8</div>
</section>

</body>
</html>
```